I need a business Card Design for my practice , i am clinical herbalist. I am a herbalist specializing in Lyme disease, autism, autoimmune diseases, difficult to cure diseasesDifficult to cure diseases. In my innovative practice i link traditional medicine, herbs with science, immunologu ,pharmacology.

Industry/Entity Type

Business

Contact Information for Business Card

My company name : OŚRODEK ZIELNIK
My name : Piotr Kaleta
Name of my profession : Fitoterapeuta
In Polish language Fitoterapeuta is Herbalist .

e-mail: piotrkaleta@osrodekzielnik.com
www.osrodek-zielnik.pl
phone : 604 587 231
My company adress : Dąbrowa Sitnicka 41 , 38-415 Łęgowice
I dont have logo .

Requirements
Nice to have
• My company

```html
<!DOCTYPE html>
<html lang="pl">
<head>
<meta charset="utf-8">
<title>Ośrodek Zielnik – wizytówka</title>
<link rel="stylesheet" href="https://fonts.googleapis.com/css2?family=Montserrat:wght@600;700&family=Open+Sans:wght@400&display=swap">
<style>
  :root{
    --stage:#e9e6e1;
    --card-light:#ffffff;
    --card-dark:#0b0b0b;
    --ink:#3b3b3b;
    --ink-dark:#6a6a6a;
    --brown:#6b5130;
    --name-brown:#6e4b1f;
    --green-dark:#4f8f3e;
    --green-light:#7cc242;
    --text:#1e1e1e;
    --muted:#7a7a7a;
  }
  *{margin:0;padding:0;box-sizing:border-box}
  html,body{width:1200px;height:1000px;overflow:hidden;background:var(--stage)}
  .stage{position:relative;width:1200px;height:1000px}
  .card{position:absolute;left:266px;width:666px;height:398px;border-radius:24px;overflow:hidden;box-shadow:0 6px 16px rgba(0,0,0,.25)}
  .card--front{top:74px;background:var(--card-light)}
  .card--back{top:534px;background:var(--card-dark)}

  .brand-mark{position:absolute;left:50%;transform:translateX(-50%);border-radius:50%}
  .card--front .brand-mark{top:34px;width:84px;height:84px;background:var(--green-light)}
  .card--back .brand-mark{top:94px;width:96px;height:96px;background:var(--green-light)}

  .brand-name{position:absolute;left:0;right:0;text-align:center;font-family:"Montserrat",sans-serif;font-weight:700;letter-spacing:.5px}
  .card--front .brand-name{top:146px;font-size:34px;color:var(--ink)}
  .card--back .brand-name{top:222px;font-size:40px;color:var(--ink-dark)}

  .person{position:absolute;right:355px;top:262px;text-align:right}
  .person__name{font-family:"Montserrat",sans-serif;font-weight:700;font-size:22px;color:var(--name-brown);letter-spacing:.5px}
  .person__role{font-family:"Open Sans",sans-serif;font-size:16px;color:var(--text);margin-top:2px}

  .divider{position:absolute;left:332px;top:246px;width:2px;height:84px;background:var(--text)}

  .contact{position:absolute;left:354px;top:242px;font-family:"Open Sans",sans-serif;font-size:16px;color:var(--text);list-style:none}
  .contact li{height:23px;line-height:23px;display:flex;align-items:center}
  .contact li.contact__address{margin-bottom:2px}
  .contact svg{width:14px;height:14px;margin-right:9px;fill:var(--name-brown)}

  .band-lines{position:absolute;left:0;top:362px;width:100%;height:5px}
  .band-lines__dark{position:absolute;left:0;width:330px;height:5px;background:var(--green-dark)}
  .band-lines__light{position:absolute;left:335px;right:0;height:5px;background:var(--green-light)}
  .band-base{position:absolute;left:0;bottom:0;width:100%;height:28px;background:var(--brown)}

  .back-note{position:absolute;left:0;right:0;top:348px;text-align:center;font-family:"Open Sans",sans-serif;font-size:16px;color:var(--muted);letter-spacing:.3px}
</style>
</head>
<body>
<main class="stage">
  <section class="card card--front">
    <div class="brand-mark"></div>
    <h1 class="brand-name">OŚRODEK ZIELNIK</h1>

    <div class="person">
      <p class="person__name">PIOTR KALETA</p>
      <p class="person__role">Fitoterapeuta</p>
    </div>
    <div class="divider"></div>
    <ul class="contact">
      <li class="contact__address">Dąbrowa Sitnicka 41, 38-415 Łęgowice</li>
      <li><svg viewBox="0 0 24 24"><path d="M3 9c0-3 4-5 9-5s9 2 9 5v2h-5V9H8v2H3zM6 12h12l2 8H4z"/></svg>604 587 231</li>
      <li><svg viewBox="0 0 24 24"><path d="M2 5h20v14H2zM3 6l9 7 9-7v2l-9 7-9-7z" fill-rule="evenodd"/></svg>piotrkaleta@osrodekzielnik.com</li>
      <li><svg viewBox="0 0 24 24"><circle cx="10" cy="10" r="8"/><path d="M12 12l9 3-4 2 3 4-2 1-3-4-2 3z" fill="#fff" stroke="#6e4b1f" stroke-width="1"/></svg>www.osrodek-zielnik.pl</li>
    </ul>

    <div class="band-lines"><span class="band-lines__dark"></span><span class="band-lines__light"></span></div>
    <div class="band-base"></div>
  </section>

  <section class="card card--back">
    <div class="brand-mark"></div>
    <h2 class="brand-name">OŚRODEK ZIELNIK</h2>
    <p class="back-note">Fitoterapeuta jest zielarzem</p>
  </section>
</main>
</body>
</html>
```